Business Card Design needed - Something Awesome!

Need a business card designed. Company is "Harbor Vane Consulting" we do consulting and also have sales automation technology.
I'm going to use thick stock or metal, something really nice... I was thinking about a QR Code on the back that would just upload my contact info to the persons contact, etc -

This is a Strategy Company with a tech feel. I'm open to ideas but really want this to be nice!

I need a template that should include:

Name | Position or Title
D: 555.203.8146
www.harborvaneconsulting.example

I'm going to attach my contact so you can use that one, I need to get this printed.

Target Market(s)

Small to mid size customers, Entrepreneurs etc.

Industry/Entity Type

Consulting, Tech, Private Equity.

Contact Information for Business Card

Name, Phone, Maybe email, URL

Font styles to use
Sans Serif

Colors

Designer to choose only greyscale colors for use in the design.

Requirements
Must have
• Fresh, Clean, stand out from the crowd - will be on thick stock or metal.
Nice to have
• Clean, simple yet impactful.
Should not have
• Not cartoonish

```html
<!DOCTYPE html>
<html lang="en">
<head>
<meta charset="utf-8">
<title>Harbor Vane Consulting – Business Cards</title>
<link href="https://fonts.googleapis.com/css2?family=Arimo:wght@400;700&display=swap" rel="stylesheet">
<style>
  :root {
    --backdrop: #8a827b;
    --card: #141414;
    --card-soft: #1c1c1d;
    --pattern: #232325;
    --accent-area: #1d1d1e;
    --text-light: #d4d4d4;
    --text-mid: #a9a9a9;
    --text-dim: #6f6f6f;
    --silver: #c9c9cb;
  }
  * { margin: 0; padding: 0; box-sizing: border-box; }
  html, body {
    width: 1200px; height: 833px; overflow: hidden;
    background: var(--backdrop);
    font-family: "Arimo", Arial, sans-serif;
  }
  .canvas { position: relative; width: 1200px; height: 833px; }

  .card {
    position: absolute;
    background: var(--card);
    box-shadow: 0 10px 28px rgba(0,0,0,0.35);
    overflow: hidden;
  }

  /* Logo side */
  .card--brand {
    left: 560px; top: 140px; width: 500px; height: 286px;
    background: var(--card-soft);
  }
  .brand-pattern {
    position: absolute; inset: 0;
    background: linear-gradient(135deg, var(--pattern), var(--card-soft) 60%, var(--pattern));
  }
  .brand-wordmark {
    position: absolute; left: 0; right: 0; top: 118px;
    text-align: center;
    font-weight: 700; font-size: 40px; letter-spacing: 3px;
    color: var(--silver);
  }

  /* Contact side */
  .card--contact {
    left: 80px; top: 450px; width: 520px; height: 300px;
    background: linear-gradient(160deg, #1b1b1b, var(--card) 55%);
  }
  .contact-accent {
    position: absolute; right: 0; bottom: 0; width: 190px; height: 230px;
    background: linear-gradient(200deg, var(--accent-area), var(--card) 70%);
  }
  .contact-name {
    position: absolute; left: 52px; top: 44px;
    font-size: 21px; color: var(--text-light); white-space: nowrap;
  }
  .contact-name strong { font-weight: 700; }
  .contact-name .divider { color: var(--text-dim); margin: 0 6px; font-weight: 400; }
  .contact-phone {
    position: absolute; left: 52px; top: 76px;
    font-size: 16px; color: var(--text-mid);
  }
  .contact-booking {
    position: absolute; left: 52px; top: 140px;
    font-size: 13px; color: var(--text-mid);
  }
  .contact-brand {
    position: absolute; left: 50px; top: 194px;
    display: flex; align-items: center; gap: 10px;
  }
  .contact-wordmark {
    font-weight: 700; font-size: 32px; letter-spacing: 1px;
    color: var(--text-dim); white-space: nowrap;
  }
  .contact-square {
    width: 44px; height: 44px; background: var(--text-dim);
  }
  .contact-url {
    position: absolute; left: 52px; top: 246px;
    font-size: 12.5px; color: var(--text-dim);
  }
</style>
</head>
<body>
<main class="canvas">

  <section class="card card--brand" aria-label="Business card, logo side">
    <div class="brand-pattern" role="img" aria-label="Subtle repeating diamond outline pattern in dark grey"></div>
    <div class="brand-wordmark">HARBOR VANE</div>
  </section>

  <section class="card card--contact" aria-label="Business card, contact side">
    <div class="contact-accent" role="img" aria-label="Faint angled outline decoration in dark grey"></div>
    <p class="contact-name"><strong>Daniel R. Okafor</strong><span class="divider">|</span><span class="title">Founder / CEO</span></p>
    <p class="contact-phone">M: 555.203.8146</p>
    <p class="contact-booking">Book a meeting</p>
    <div class="contact-brand">
      <p class="contact-wordmark">HARBOR VANE</p>
      <div class="contact-square"></div>
    </div>
    <p class="contact-url">www.harborvaneconsulting.example</p>
  </section>

</main>
</body>
</html>
```